Every sort of trade everysortoftrade.ca

Website for company offering Every sort of trade
Welding/Fabrication/Metal repairs/Metal building, Electrical repairs and installations, Plumbing and Heating, Renovations, Flooring, Paiting, and other services

We need a very clean and professional website outlining the many services we have

We would like each type of service to have its own page, with images of those types of services on those pages.

Then in the future, we can update those pages with projects we have done of those types.

Every Sort of Trade . CA

Located in Ridgeford, Westland Valley, offering services region wide

Welding/Fabrication/Repair/Building - Steel and metals
Electrical contractor - Journeyman , small or large projects
Plumbing and Heating
Renovations
Flooring
Painting
Other services - storage, trucking, delivery, etc

business and residential services

Contractor

Coded - Design and coding required

5+ page

Sans Serif

3176b5
0253a1
85acd3
85abd2
cedeed
ffffff

Must have
• Clean
• Professional
• Easy of updating text and images

```html
<!DOCTYPE html>
<html lang="en">
<head>
<meta charset="utf-8">
<title>Every Sort of Trade</title>
<link href="https://fonts.googleapis.com/css2?family=Open+Sans:wght@400;600;700&family=Raleway:wght@400;600;700;800&display=swap" rel="stylesheet">
<style>
:root{
  --blue:#3176b5;
  --navy:#0253a1;
  --sky:#85acd3;
  --pale:#cedeed;
  --white:#ffffff;
  --ink:#222b36;
  --text:#5a6470;
  --orange:#f26b1d;
  --dark:#2a2f36;
  --line:#e3e8ee;
}
*{box-sizing:border-box;margin:0;padding:0}
html,body{width:1200px;height:4144px;overflow:hidden}
body{font-family:"Open Sans",Arial,sans-serif;color:var(--text);background:var(--white);font-size:14px;line-height:1.6}
h1,h2,h3,h4{font-family:"Raleway",Arial,sans-serif}

/* header */
.topbar{height:112px;position:relative;background:var(--navy)}
.topbar .brand-panel{position:absolute;left:0;top:0;width:470px;height:112px;background:var(--white);clip-path:polygon(0 0,100% 0,88% 100%,0 100%)}
.brand{position:absolute;left:64px;top:22px;display:flex;align-items:center;gap:14px}
.brand-mark{width:52px;height:52px;background:var(--navy)}
.brand-name{font-family:"Raleway",sans-serif;font-weight:800;font-size:26px;line-height:1.05;color:var(--navy);text-transform:uppercase}
.contact-blocks{position:absolute;right:72px;top:26px;display:flex;gap:48px;align-items:center;color:var(--white)}
.cblock{display:flex;gap:12px;align-items:center}
.cblock svg{width:36px;height:36px}
.cblock b{display:block;font-family:"Raleway",sans-serif;font-size:20px;font-weight:600;line-height:1.1}
.cblock span{font-size:12px;opacity:.85}
.quote-btn{background:var(--orange);color:var(--white);font-weight:700;font-size:14px;padding:10px 18px;border-radius:3px}
.nav{height:38px;border-bottom:1px solid var(--line);position:relative;background:var(--white)}
.nav ul{list-style:none;display:flex;position:absolute;left:72px;top:0}
.nav li{font-family:"Raleway",sans-serif;font-size:12px;font-weight:700;color:var(--navy);text-transform:uppercase;padding:0 24px;line-height:36px}
.nav li.active{border-bottom:3px solid var(--blue)}
.search{position:absolute;right:72px;top:6px;display:flex;align-items:center;gap:10px}
.search div{width:180px;height:26px;border:1px solid var(--line);font-size:11px;padding:4px 10px;color:#9aa3ad}

/* hero */
.hero{height:562px;position:relative;background:linear-gradient(100deg,#7d8a98 0%,#c9d2dc 40%,#e6ebf0 60%,#b7c2ce 100%)}
.hero-text{position:absolute;left:64px;top:170px;color:var(--white)}
.hero-text .hello{font-family:"Raleway",sans-serif;font-weight:700;font-size:34px;line-height:1}
.hero-text h1{font-weight:800;font-size:54px;line-height:1.15;color:var(--white)}
.hero-text p{width:360px;font-size:13px;margin:12px 0 18px;line-height:1.55}
.btn{display:inline-block;background:var(--navy);color:var(--white);font-weight:700;font-size:13px;padding:10px 22px;border-radius:3px;font-family:"Raleway",sans-serif;text-transform:uppercase}
.hero-text .btn{text-transform:none}

/* section head */
.sec-head{text-align:center}
.kicker{font-size:12px;color:var(--text)}
.sec-head h2{font-weight:800;font-size:28px;text-transform:uppercase;color:var(--ink);margin-top:4px}
.sec-head .rule{width:100px;height:3px;background:var(--blue);margin:10px auto 0}
.dark .kicker,.dark h2{color:var(--white)}
.dark .rule{background:var(--white)}

/* about */
.about{height:500px;padding-top:52px;text-align:center}
.about .home-ico{width:36px;height:36px;margin:0 auto 14px}
.about h2{font-size:28px;font-weight:800;text-transform:uppercase;color:var(--ink)}
.about .rule{width:100px;height:3px;background:var(--blue);margin:10px auto 30px}
.about p{width:980px;margin:0 auto 22px;font-size:13.5px;line-height:1.75}

/* services */
.services{height:660px;background:var(--navy);padding-top:58px}
.svc-row{display:flex;width:1056px;margin:40px auto 0;background:var(--white)}
.svc{width:352px;position:relative;padding-bottom:14px}
.svc .ph{height:228px}
.svc .ico{position:absolute;left:50%;top:204px;width:48px;height:48px;margin-left:-24px;background:var(--white);border-radius:50%;display:flex;align-items:center;justify-content:center}
.svc h3{text-align:center;font-size:16px;font-weight:700;color:var(--ink);text-transform:uppercase;margin-top:36px}
.svc .sub{text-align:center;font-size:12px;color:#8a939d}
.svc.featured .plus{position:absolute;left:50%;top:90px;margin-left:-26px;width:52px;height:52px;border:2px solid var(--white);border-radius:50%}
.svc.featured .meta{display:flex;justify-content:space-around;border-top:1px solid var(--line);margin-top:12px;padding-top:8px;font-size:11px;color:#8a939d}
.pager{display:flex;justify-content:center;gap:6px;margin-top:40px}
.pager span{width:38px;height:38px;background:var(--white);display:flex;align-items:center;justify-content:center}

/* work */
.work{height:692px;padding-top:58px}
.tabs{display:flex;justify-content:center;gap:40px;margin-top:40px;font-size:13px;color:var(--ink)}
.tabs span:first-child{color:var(--navy);font-weight:600}
.gallery{display:flex;gap:12px;width:1032px;margin:40px auto 0}
.gallery .tile{width:197px;height:256px;position:relative}
.gallery .tile.on .label{position:absolute;inset:0;background:rgba(2,83,161,.78);color:var(--white);font-family:"Raleway",sans-serif;font-weight:800;font-size:20px;display:flex;align-items:center;justify-content:center}
.work .center{text-align:center;margin-top:40px}

/* banner */
.banner{height:388px;background:linear-gradient(180deg,#3a3f46 0%,#20252b 100%);text-align:center;color:var(--white);padding-top:70px}
.banner .welcome{font-size:13px;letter-spacing:1px;text-transform:uppercase}
.banner h2{font-weight:800;font-size:54px;text-transform:uppercase;letter-spacing:3px;line-height:1.2}
.banner h2 em{font-style:normal;color:var(--blue)}
.banner .rule{width:140px;height:3px;background:var(--white);margin:18px auto 26px}
.banner h3{font-weight:700;font-size:34px;text-transform:uppercase;letter-spacing:2px;line-height:1.25}

/* team */
.team{height:640px;padding-top:52px}
.team-row{display:flex;gap:28px;width:1056px;margin:60px auto 0}
.member{width:514px;height:330px;display:flex;box-shadow:0 2px 12px rgba(0,0,0,.1)}
.member .info{width:254px;padding:38px 24px;border-left:4px solid var(--blue)}
.member h4{font-size:24px;font-weight:600;color:var(--ink);line-height:1.1}
.member .role{font-size:12px;color:#8a939d;margin-bottom:18px}
.member p{font-size:12px;line-height:1.6}
.socials{display:flex;gap:6px;margin-top:22px}
.socials span{width:26px;height:26px;border:1px solid var(--line)}
.member .ph{width:260px}

/* contact */
.contact{height:472px;background:var(--navy);color:var(--white);padding:56px 72px 0;position:relative}
.contact h2{font-weight:700;font-size:30px;text-transform:uppercase}
.contact .lead{width:380px;font-size:12.5px;margin-top:10px;line-height:1.55}
.crow{display:flex;align-items:center;gap:14px;margin-top:26px;font-size:12.5px}
.crow i{width:42px;height:42px;border:2px solid var(--white);border-radius:50%;display:flex;align-items:center;justify-content:center;flex:none}
.form{position:absolute;left:460px;top:220px;width:250px}
.field{height:36px;border:1px solid var(--sky);margin-bottom:14px;padding:8px 12px;font-size:12px}
.submit{display:inline-block;background:#1d1f22;color:var(--white);font-size:11px;font-weight:700;padding:8px 16px;text-transform:uppercase}
.message{position:absolute;left:732px;top:220px;width:210px;height:150px;border:1px solid var(--sky);padding:8px 12px;font-size:12px}

.footer{height:72px;background:#0a3f7c;color:var(--white);text-align:center;font-size:12px;line-height:72px}
</style>
</head>
<body>

<header>
  <div class="topbar">
    <div class="brand-panel"></div>
    <div class="brand">
      <div class="brand-mark"></div>
      <div class="brand-name">Every Sort<br>of Trade</div>
    </div>
    <div class="contact-blocks">
      <div class="cblock">
        <svg viewBox="0 0 24 24" fill="none" stroke="#fff" stroke-width="1.8"><path d="M12 22s7-7 7-12a7 7 0 1 0-14 0c0 5 7 12 7 12z"/><circle cx="12" cy="10" r="2.5"/></svg>
        <div><b>Address</b><span>1208 Ridgeline Way, Ridgeford</span></div>
      </div>
      <div class="cblock">
        <svg viewBox="0 0 24 24" fill="none" stroke="#fff" stroke-width="1.8"><path d="M5 3h4l2 5-3 2a12 12 0 0 0 6 6l2-3 5 2v4a2 2 0 0 1-2 2A17 17 0 0 1 3 5a2 2 0 0 1 2-2z"/></svg>
        <div><b>Call Us</b><span>(555) 014-2260</span></div>
      </div>
      <div class="quote-btn">Get a Quote</div>
    </div>
  </div>
  <nav class="nav">
    <ul>
      <li class="active">Home</li><li>About</li><li>Who we are</li><li>Service</li><li>Our Work</li><li>News</li><li>Contact us</li>
    </ul>
    <div class="search">
      <div>Search ...</div>
      <svg width="16" height="16" viewBox="0 0 24 24" fill="none" stroke="#222b36" stroke-width="2.5"><circle cx="10" cy="10" r="7"/><path d="M15 15l6 6"/></svg>
    </div>
  </nav>
</header>

<section class="hero" role="img" aria-label="Two engineers in hard hats reviewing building plans inside a construction site">
  <div class="hero-text">
    <div class="hello">HELLO!</div>
    <h1>WE ARE TRADEWORKS</h1>
    <p>Skilled trades under one roof, serving homes and businesses across the region. From steel work to paint, we bring the right crew to every job, on time and built to last for years.</p>
    <span class="btn">Read More</span>
  </div>
</section>

<section class="about">
  <svg class="home-ico" viewBox="0 0 24 24" fill="none" stroke="#0253a1" stroke-width="2"><path d="M3 11l9-8 9 8v10H3z"/><rect x="9" y="13" width="6" height="8"/></svg>
  <h2>We are the leader in the construction!</h2>
  <div class="rule"></div>
  <p>With over 20 years of experience and a real focus on customer satisfaction, you can rely on us for your next renovation, driveway job or home repair. We are proud to be a professional service for private and commercial customers. Our crews handle welding, electrical, plumbing, heating, flooring and painting, and every job is planned with care from the first visit to the final walkthrough. We keep our sites clean, our quotes clear and our schedules honest.</p>
  <p>It began in a small local shop with a single welding rig and a truck, and it has grown into a full team of certified tradespeople working across the region, for small and large projects alike.</p>
  <span class="btn">Read More</span>
</section>

<section class="services dark">
  <div class="sec-head">
    <div class="kicker">Every Sort of Trade - Build your feature!</div>
    <h2>Our Services</h2>
    <div class="rule"></div>
  </div>
  <div class="svc-row">
    <div class="svc">
      <div class="ph" role="img" aria-label="Modern steel and brick building facade" style="background:linear-gradient(160deg,#8aa6c4,#4a5b6d 60%,#9a6a4e)"></div>
      <div class="ico"><svg width="22" height="22" viewBox="0 0 24 24" fill="none" stroke="#0253a1" stroke-width="2"><path d="M4 6h16M12 6v14M8 20h8"/></svg></div>
      <h3>Steel and Metals</h3><div class="sub">Pre Work</div>
    </div>
    <div class="svc featured">
      <div class="ph" role="img" aria-label="Electrician in hard hat working on wiring" style="background:linear-gradient(160deg,#2a2f36,#5a5040 70%,#3a3f46)"></div>
      <div class="plus"></div>
      <div class="ico"><svg width="22" height="22" viewBox="0 0 24 24" fill="none" stroke="#0253a1" stroke-width="2"><path d="M13 2L5 14h6l-1 8 8-12h-6z"/></svg></div>
      <h3>Electrical Contractor</h3><div class="sub">Pre Work</div>
      <div class="meta"><span>Small projects</span><span>Large projects</span></div>
    </div>
    <div class="svc">
      <div class="ph" role="img" aria-label="Roofer renovating a house roof under blue sky" style="background:linear-gradient(160deg,#6fa4d8,#9a4e3a 70%,#c7d2dc)"></div>
      <div class="ico"><svg width="22" height="22" viewBox="0 0 24 24" fill="none" stroke="#0253a1" stroke-width="2"><path d="M3 11l9-8 9 8v10H3z"/></svg></div>
      <h3>Renovations</h3><div class="sub">Pre Work</div>
    </div>
  </div>
  <div class="pager">
    <span><svg width="14" height="14" viewBox="0 0 24 24" fill="none" stroke="#0253a1" stroke-width="3"><path d="M15 4l-8 8 8 8"/></svg></span>
    <span><svg width="14" height="14" viewBox="0 0 24 24" fill="none" stroke="#0253a1" stroke-width="3"><path d="M9 4l8 8-8 8"/></svg></span>
  </div>
</section>

<section class="work">
  <div class="sec-head">
    <div class="kicker">Every Sort of Trade - Build your feature!</div>
    <h2>Featured Work</h2>
    <div class="rule"></div>
  </div>
  <div class="tabs">
    <span>Welding/Fabrication/Repair</span><span>Building Steel and metals</span><span>Plumbing and Heating</span><span>Renovations</span><span>Flooring</span><span>Painting</span>
  </div>
  <div class="gallery">
    <div class="tile on" role="img" aria-label="Construction site project" style="background:linear-gradient(160deg,#6a8fb5,#3a5878)"><span class="label">Construction</span></div>
    <div class="tile" role="img" aria-label="Workers in hard hats on site" style="background:linear-gradient(160deg,#c9d4de,#7c8a98)"></div>
    <div class="tile" role="img" aria-label="Engineers checking plans together" style="background:linear-gradient(160deg,#d6dde4,#e0a54a 70%,#8c9aa8)"></div>
    <div class="tile" role="img" aria-label="Builder in hi-vis vest at a brick wall" style="background:linear-gradient(160deg,#b5643e,#d9c23a 60%,#7a4a32)"></div>
    <div class="tile" role="img" aria-label="Tradesman using a power tool" style="background:linear-gradient(160deg,#5a5a5a,#d8a53a 60%,#3a3a3a)"></div>
  </div>
  <div class="center"><span class="btn">View All Work</span></div>
</section>

<section class="banner" role="img" aria-label="Dark construction site at dusk with steel framework">
  <div class="welcome">Well Come</div>
  <h2>Every Sort of <em>Trade</em></h2>
  <div class="rule"></div>
  <h3>We'll help manage your<br>site very easy</h3>
</section>

<section class="team">
  <div class="sec-head">
    <div class="kicker">Every Sort of Trade - Build your feature!</div>
    <h2>Our Team</h2>
    <div class="rule"></div>
  </div>
  <div class="team-row">
    <div class="member">
      <div class="info">
        <h4>Marla Denholm</h4>
        <div class="role">Head of Interior Design</div>
        <p>Marla leads our renovation and flooring crews, turning rough plans into finished rooms that clients love to live and work in.</p>
        <div class="socials"><span></span><span></span><span></span><span></span></div>
      </div>
      <div class="ph" role="img" aria-label="Portrait of team member" style="background:linear-gradient(160deg,#3a2e28,#a87a5e 60%,#2a2420)"></div>
    </div>
    <div class="member">
      <div class="info">
        <h4>Curtis Renwick</h4>
        <div class="role">Operations Director</div>
        <p>Curtis runs scheduling and site safety across the region, keeping welders, electricians and plumbers moving on every project.</p>
        <div class="socials"><span></span><span></span><span></span><span></span></div>
      </div>
      <div class="ph" role="img" aria-label="Portrait of team member" style="background:linear-gradient(160deg,#e8e8e8,#9a7a66 60%,#3a2e28)"></div>
    </div>
  </div>
</section>

<section class="contact">
  <h2>Get in Touch</h2>
  <p class="lead">We are very approachable and would love to speak to you. Feel free to call, send us an email, Tweet us or simply complete the enquiry form.</p>
  <div class="crow"><i><svg width="18" height="18" viewBox="0 0 24 24" fill="none" stroke="#fff" stroke-width="2"><path d="M12 22s7-7 7-12a7 7 0 1 0-14 0c0 5 7 12 7 12z"/><circle cx="12" cy="10" r="2.5"/></svg></i><span>Ridgeford, Westland Valley, offering services<br>region wide</span></div>
  <div class="crow"><i><svg width="18" height="18" viewBox="0 0 24 24" fill="none" stroke="#fff" stroke-width="2"><rect x="3" y="5" width="18" height="14"/><path d="M3 6l9 7 9-7"/></svg></i><span>info@everysortoftrade.ca</span></div>
  <div class="crow"><i><svg width="18" height="18" viewBox="0 0 24 24" fill="none" stroke="#fff" stroke-width="2"><path d="M5 3h4l2 5-3 2a12 12 0 0 0 6 6l2-3 5 2v4a2 2 0 0 1-2 2A17 17 0 0 1 3 5a2 2 0 0 1 2-2z"/></svg></i><span>+1 555 014 2260</span></div>
  <div class="form">
    <div class="field">Name</div>
    <div class="field">Number</div>
    <div class="field">Mail</div>
    <span class="submit">Submit</span>
  </div>
  <div class="message">Message</div>
</section>

<footer class="footer">All rights reserved Copyright © 2017 Every Sort of Trade . CA</footer>

</body>
</html>
```